Convert Design into Adobe Ilustrator (Ai) File - Product Label

Convert the provided Graphic Design into an Adobe Illustrator (Ai) File for a Product Label. This Ai file needs to be fully editable, organised into logical layers and well structured. The text needs to be outlined for printing. This is for a POUCH DESIGN. The pouch dimensions file is attached. We'll share the details for the other side of the pouch if you are interested in accepting this project. Thanks.

Industry/Entity Type

FOOD SUPPLEMENTS

```html
<!DOCTYPE html>
<html lang="en">
<head>
<meta charset="utf-8">
<title>Tide &amp; Theory – Marine Collagen Complex Pouch Front</title>
<link rel="stylesheet" href="https://fonts.googleapis.com/css2?family=Tinos:wght@400&display=swap">
<style>
  :root {
    --stage-side: #dcdcdc;
    --stage-centre: #ffffff;
    --pouch-navy: #2f3f68;
    --pouch-navy-light: #36497c;
    --pouch-navy-dark: #2a385e;
    --accent-tan: #e3b47f;
    --rule-tan: #b59a7e;
    --text-white: #ffffff;
    --dieline-blue: #1aa3e0;
    --border-faint: #4a5a86;
  }
  html, body {
    margin: 0;
    padding: 0;
    width: 1200px;
    height: 1200px;
    overflow: hidden;
    background: var(--stage-side);
  }
  .canvas {
    display: block;
    width: 1200px;
    height: 1200px;
  }
  .stage-side { fill: var(--stage-side); }
  .stage-centre { fill: var(--stage-centre); }
  .pouch-body { fill: url(#pouchTone); }
  .pouch-border { fill: none; stroke: var(--border-faint); stroke-width: 1.2; }
  .dieline { fill: none; stroke: var(--dieline-blue); stroke-width: 1.4; stroke-dasharray: 5 4; }
  .dieline-marker { fill: var(--dieline-blue); }
  .brand-rule { stroke: var(--rule-tan); stroke-width: 1.4; }

  .serif { font-family: "Tinos", "Times New Roman", serif; }
  .brand-name { fill: var(--accent-tan); font-size: 37px; letter-spacing: 6px; }
  .product-title { fill: var(--accent-tan); font-size: 57px; }
  .ingredients { fill: var(--text-white); font-size: 32px; }
  .serving-info { fill: var(--text-white); font-size: 18.5px; }
  .feature-list { fill: var(--text-white); font-size: 18px; }
  .net-content { fill: var(--text-white); font-size: 18px; }
</style>
</head>
<body>
<svg class="canvas" viewBox="0 0 1200 1200" xmlns="http://www.w3.org/2000/svg">
  <defs>
    <radialGradient id="pouchTone" cx="50%" cy="45%" r="70%">
      <stop offset="0%" stop-color="var(--pouch-navy-light)"/>
      <stop offset="60%" stop-color="var(--pouch-navy)"/>
      <stop offset="100%" stop-color="var(--pouch-navy-dark)"/>
    </radialGradient>
  </defs>

  <!-- Presentation board -->
  <rect class="stage-side" x="0" y="0" width="1200" height="1200"/>
  <rect class="stage-centre" x="85" y="0" width="1028" height="1200"/>

  <!-- Pouch front panel -->
  <rect class="pouch-body" x="212.5" y="90" width="777.5" height="1020"
        role="img" aria-label="Navy pouch background with a soft flowing wave texture"/>
  <rect class="pouch-border" x="245" y="112.5" width="712.5" height="970" rx="12"/>

  <!-- Dieline: seals, tear notches and gusset -->
  <g class="dieline-group">
    <line class="dieline" x1="277.5" y1="112.5" x2="277.5" y2="1082.5"/>
    <line class="dieline" x1="925" y1="112.5" x2="925" y2="1082.5"/>
    <line class="dieline" x1="245" y1="206" x2="957.5" y2="206"/>
    <line class="dieline" x1="245" y1="231" x2="957.5" y2="231"/>
    <line class="dieline" x1="245" y1="256" x2="957.5" y2="256"/>
    <line class="dieline" x1="245" y1="879" x2="277.5" y2="879"/>
    <line class="dieline" x1="925" y1="879" x2="957.5" y2="879"/>
    <path class="dieline" d="M245 879 Q600 1216 957.5 879"/>
    <path class="dieline-marker" d="M246 186 L252 190 L246 194 Z"/>
    <path class="dieline-marker" d="M956 186 L950 190 L956 194 Z"/>
  </g>

  <!-- Brand -->
  <text class="serif brand-name" x="600" y="340" text-anchor="middle">TIDE &amp; THEORY</text>
  <line class="brand-rule" x1="316" y1="377.5" x2="885" y2="377.5"/>

  <!-- Product title -->
  <text class="serif product-title" x="319">
    <tspan x="319" y="456">MARINE</tspan>
    <tspan x="319" y="516">COLLAGEN</tspan>
    <tspan x="319" y="575">COMPLEX</tspan>
  </text>

  <!-- Ingredients -->
  <text class="serif ingredients">
    <tspan x="319" y="704">Marine Collagen,</tspan>
    <tspan x="319" y="749">Vitamin C</tspan>
    <tspan x="319" y="791">&amp; Hyaluronic Acid</tspan>
  </text>
  <text class="serif serving-info" x="319" y="852">30 servings | 13.500mg per serving</text>

  <!-- Feature list -->
  <text class="serif feature-list">
    <tspan x="701" y="691">Low molecular weight</tspan>
    <tspan x="701" y="736">2000 kDa</tspan>
    <tspan x="701" y="782">Unflavoured</tspan>
    <tspan x="701" y="827">Sourced from</tspan>
    <tspan x="701" y="852">wild caught fish</tspan>
  </text>

  <!-- Net content -->
  <text class="serif net-content" x="600" y="996" text-anchor="middle">Food Supplement | ℮ 375g</text>
</svg>
</body>
</html>
```